Support Welcome Packet Redesign

Looking to redesign our current "welcome packet" that we send to our new customers to help them understand our support service. It is currently in Microsoft Word and would like to remain in either word or publisher. Something that we can easily edit, as the content adjusts based on the customer needs. We want this document to be simple and understandable as it should be something our customers can reference at any time during our contract and easy to navigate.

Target Market(s)

Current Customers. Healthcare, Oil & Gas, Transportation, etc.

Industry/Entity Type

It Service

Font styles to use
Sans Serif

Requirements
Must have
• Table of Contents, bluQuay Logo and current content
Nice to have
• Easy navigation. Redone final page (contact info)

Files

```html
<!DOCTYPE html>
<html lang="en">
<head>
<meta charset="utf-8">
<title>bluQuay Welcome Packet</title>
<link rel="stylesheet" href="https://fonts.googleapis.com/css2?family=Open+Sans:wght@400;600;800&display=swap">
<style>
  :root{
    --canvas:#ffffff;
    --cover-blue:#1f74bd;
    --cover-teal:#2f8d8c;
    --leaf-green:#8cc043;
    --band-blue:#8ea7d6;
    --band-green:#c7d99b;
    --band-teal:#8aa6a8;
    --title-blue:#2a7cc1;
    --rule:#e3e6ea;
    --ink:#333a40;
    --logo-orange:#e98b2a;
    --hand-tones:linear-gradient(135deg,#2f62b8 0%,#8cc043 55%,#f2b5a0 100%);
  }
  *{box-sizing:border-box;margin:0;padding:0}
  html,body{width:1200px;height:849px;overflow:hidden;background:var(--canvas)}
  body{position:relative;font-family:"Open Sans",sans-serif;color:var(--ink)}
  .page{position:absolute;top:180px;width:340px;height:460px;overflow:hidden;box-shadow:0 6px 18px rgba(0,0,0,.18);background:#fff}
  .page--cover{left:40px;background:var(--cover-blue)}
  .page--contents{left:430px}
  .page--services{left:820px}
  .page svg.bg{position:absolute;inset:0;width:100%;height:100%}

  /* cover */
  .cover__map{position:absolute;left:0;top:120px;width:340px;height:200px;background:var(--cover-teal)}
  .cover__title{position:absolute;left:12px;top:160px;height:62px;line-height:62px;font-weight:800;font-size:52px;color:#fff;letter-spacing:1px;transform:rotate(-28deg);transform-origin:left bottom;white-space:nowrap}
  .cover__handshake{position:absolute;left:60px;top:190px;width:200px;height:140px;border-radius:40px 60px 30px 70px;background:var(--hand-tones)}
  .cover__brand{position:absolute;left:150px;top:345px;text-align:left;color:#fff}
  .brand{display:flex;align-items:center;gap:6px}
  .brand__mark{width:22px;height:22px;background:var(--logo-orange)}
  .brand__name{font-weight:600;font-size:24px;color:var(--logo-orange)}
  .cover__sub{font-size:10px;color:var(--band-green);margin:2px 0 0 28px}

  /* inner pages */
  .page__title{position:absolute;right:22px;font-size:21px;color:var(--title-blue);font-weight:400}
  .toc{position:absolute;left:110px;top:150px;width:190px;font-size:6.5px;line-height:1.55;list-style:none}
  .toc li{display:flex;justify-content:space-between}
  .toc li span:first-child{flex:1;overflow:hidden;white-space:nowrap}
  .toc li span:first-child::after{content:" ....................................................................."}
  .summary{position:absolute;left:26px;top:305px;width:290px;font-size:6.8px;line-height:1.5}
  .intro{position:absolute;left:28px;top:118px;width:290px;font-size:6.8px;line-height:1.45}
  .services{position:absolute;left:34px;top:172px;width:270px;font-size:6px;list-style:none}
  .services li{margin-bottom:6px;line-height:1.4}
  .services li::before{content:"• "}
  .page__foot{position:absolute;left:0;right:0;bottom:20px;text-align:center}
  .page__foot .brand{justify-content:center}
  .page__foot .brand__mark{width:9px;height:9px}
  .page__foot .brand__name{font-size:10px}
  .page__foot p{font-size:4.5px;color:#fff;margin-top:2px}
</style>
</head>
<body>

<section class="page page--cover">
  <svg class="bg" viewBox="0 0 340 460" aria-hidden="true">
    <path d="M0 0H340V20C240 70 120 120 0 170Z" fill="#1a67ad"/>
    <path d="M230 120C280 90 320 60 340 30V70C310 95 270 115 230 120Z" fill="var(--leaf-green)"/>
    <path d="M0 330C120 300 240 290 340 320V460H0Z" fill="#1c6cb4"/>
    <path d="M120 460C150 400 220 350 340 340V360C240 370 180 410 160 460Z" fill="var(--leaf-green)"/>
  </svg>
  <div class="cover__map" role="img" aria-label="Teal world map backdrop"></div>
  <div class="cover__handshake" role="img" aria-label="Illustration of two clasped hands in blue, green and skin tones"></div>
  <div class="cover__title">WELCOME</div>
  <div class="cover__brand">
    <div class="brand"><span class="brand__mark"></span><span class="brand__name">bluQuay</span></div>
    <p class="cover__sub">Technology Corp.</p>
  </div>
</section>

<section class="page page--contents">
  <svg class="bg" viewBox="0 0 340 460" aria-hidden="true">
    <g stroke="var(--rule)" stroke-width="1"><line x1="68" y1="0" x2="68" y2="460"/><line x1="136" y1="0" x2="136" y2="460"/><line x1="204" y1="0" x2="204" y2="460"/><line x1="272" y1="0" x2="272" y2="460"/></g>
    <path d="M0 0H340V90C230 95 140 100 0 125Z" fill="var(--band-teal)"/>
    <path d="M120 110C220 80 300 60 340 20V70C290 95 210 105 120 110Z" fill="var(--band-green)"/>
    <path d="M0 0H340V25C250 60 130 80 0 90Z" fill="var(--band-blue)"/>
    <path d="M40 290C120 250 240 235 340 240V280C240 275 140 280 40 290Z" fill="var(--band-blue)"/>
    <path d="M0 430C100 400 220 390 340 370V460H0Z" fill="var(--band-blue)"/>
    <path d="M0 420C100 395 220 385 340 360V372C220 392 110 405 0 432Z" fill="var(--band-green)"/>
  </svg>
  <h2 class="page__title" style="top:38px">Table of contents</h2>
  <ul class="toc">
    <li><span>Table of Contents Document Summary</span><span>3</span></li>
    <li><span>Services Summary</span><span>4</span></li>
    <li><span>Support Information</span><span>5</span></li>
    <li><span>bluQuay Support Teams and Escalation Path</span><span>5</span></li>
    <li><span>bluQuay Support Escalation Matrix</span><span>6</span></li>
    <li><span>Priority Levels</span><span>6</span></li>
    <li><span>Escalation Guidelines</span><span>7</span></li>
    <li><span>bluQuay Support Contact Information</span><span>8</span></li>
    <li><span>bluQuay Support</span><span>9</span></li>
  </ul>
  <h2 class="page__title" style="top:252px">Document Summary</h2>
  <p class="summary">This document is being provided to you, our valued customer, as a guided summary to enable the use of your environment effectively. Within the upcoming pages you will find helpful information pertaining to inventory, support team escalation procedures and contact information. We welcome you to the next level of efficiency. To ensure your company is running as proficient and robustly as possible we are happy to guide you down any necessary path. Your success is our vision.</p>
  <div class="page__foot">
    <div class="brand"><span class="brand__mark"></span><span class="brand__name">bluQuay</span></div>
    <p>bluQuay Technology · 100 Harbor Way · (555) 010-0199 · bluquay-help.com</p>
  </div>
</section>

<section class="page page--services">
  <svg class="bg" viewBox="0 0 340 460" aria-hidden="true">
    <g stroke="var(--rule)" stroke-width="1"><line x1="68" y1="0" x2="68" y2="460"/><line x1="136" y1="0" x2="136" y2="460"/><line x1="204" y1="0" x2="204" y2="460"/><line x1="272" y1="0" x2="272" y2="460"/></g>
    <path d="M0 0H340V60C240 70 120 80 0 105Z" fill="var(--band-teal)"/>
    <path d="M120 90C220 70 300 55 340 20V55C290 80 210 90 120 90Z" fill="var(--band-green)"/>
    <path d="M0 0H340V20C250 50 130 70 0 70Z" fill="var(--band-blue)"/>
    <path d="M0 415C100 400 220 395 340 410V460H0Z" fill="var(--band-blue)"/>
    <path d="M0 405C110 385 230 385 340 400V412C230 396 110 396 0 417Z" fill="var(--band-green)"/>
  </svg>
  <h2 class="page__title" style="top:18px">Services Summary</h2>
  <p class="intro">The summary of services that bluQuay is supporting are listed below. Our goal is to assist you in clearly understanding these services. For information on how to use your services, please go to https://help.bluquay-desk.com/en-us or feel free to contact us directly for additional support.</p>
  <ul class="services">
    <li>Hosted Mailhub</li>
    <li>Hosted Linkchat</li>
    <li>Hosted Servers</li>
    <li>Hosted email security with Shieldwise Antivirus</li>
    <li>Server Backups</li>
    <li>K4 Service Management System</li>
    <li>Hosted DocPoint</li>
    <li>Assisted in terminal server configuration (supported during implementation – not a managed service)</li>
    <li>Netvale Configuration (supported during implementation – not a managed service)</li>
  </ul>
  <div class="page__foot">
    <div class="brand"><span class="brand__mark"></span><span class="brand__name">bluQuay</span></div>
    <p>bluQuay Technology · 100 Harbor Way · (555) 010-0199 · bluquay-help.com</p>
  </div>
</section>

</body>
</html>
```